Interior Design & Furniture E commerce Website Design

I need a cutting edge website design, this is for Interior Design Services as well as eCommerce for furniture and home decor www.lorivelhomestudio.com
Here is a sample of the concept behind the site.
I am a furniture & Interior Designer, want to create a life style brand.
Will offer Interior Design Services : Commercial & Residential (this portion will be a catalog or portfolio type)
The eCommerce side will sell, Furniture, Lighting, Decor, Gifts, Textiles, will also be offering trade so that could be at bottom of site. I also like the concept of concierge as where all the info falls under: shipping, etc..

*Please make sure to make the eCommerce prominent.

Hello Designers, I also would like to possibly update my logo, the current one I like but don't Love.

Target Market(s)

High end customers with disposable income, who also appreciate quality and unique furniture & design

Number of Pages Required

5+ page

Colors
0255a3
f37122

Requirements
Must have
• Room Planer: I will be using this tool http://qtstudio.varnelbex.com/room-planner.inc
• Live Chat
• Will be offering 3d renderings for spaces as well as Virtual Reality
• The image I loaded that looks like copper, I would like to have that as a color on the site with the texture: so the colors are Blue and copper. Would like the site to be user friendly and interactive
• http://qtstudio.varnelbex.com/ (this is the current site in development, so we will be offering Design your own, Trends, inspiration, etc...
• I have included a headshot to use for now about me. or about us.
• I also included several actual project installation (residential and commercial) as well as a variety of my furniture items
• I have Included an old Bio and some articles I would like to show case in a Press Area
• I would also like to include a section for Events (Giving back )I do a lot of charity events 1-2 a year and would like to showcase that as well
• *Please make the store (ecommerce prominent )

```html
<!DOCTYPE html>
<html lang="en">
<head>
<meta charset="utf-8">
<title>Lorivel Home Studio</title>
<link rel="stylesheet" href="https://fonts.googleapis.com/css2?family=Roboto:wght@400;500;700&display=swap">
<style>
:root{
  --blue:#0255a3;
  --orange:#f37122;
  --ink:#222;
  --muted:#666;
  --light:#f1f1f1;
  --hero:#e9e9e9;
  --footer:#232323;
  --footer-deep:#1a1a1a;
  --white:#fff;
}
*{box-sizing:border-box;margin:0;padding:0}
html,body{width:1200px;height:5028px;overflow:hidden}
body{font-family:"Roboto",Arial,sans-serif;color:var(--ink);background:var(--white);position:relative}
.abs{position:absolute}
.section-title{position:absolute;left:0;width:1200px;text-align:center;font-size:30px;font-weight:700;color:var(--ink)}
.btn{position:absolute;background:var(--blue);color:var(--white);font-size:13px;display:flex;align-items:center;justify-content:center}
.photo{position:absolute}

/* top bar */
.topbar{position:absolute;left:0;top:0;width:1200px;height:28px;background:var(--white);border-bottom:1px solid #eee;font-size:11px;color:var(--orange)}
.topbar .phone{position:absolute;left:120px;top:7px}
.topbar .social{position:absolute;left:248px;top:7px;display:flex;gap:8px}
.topbar .social span{width:13px;height:13px;border-radius:50%;background:var(--orange)}
.topbar .auth{position:absolute;right:120px;top:5px;display:flex;gap:10px}
.topbar .auth span{padding:2px 12px;font-size:11px;color:var(--white)}
.auth .signin{background:var(--orange)}
.auth .login{background:var(--blue)}

/* nav */
.nav{position:absolute;left:0;top:28px;width:1200px;height:112px;background:var(--white)}
.brand{position:absolute;left:120px;top:22px;display:flex;align-items:center;gap:10px}
.brand .mark{width:44px;height:44px;background:var(--orange)}
.brand .name{font-size:15px;font-weight:700;color:var(--orange);line-height:1.1;width:90px}
.menu{position:absolute;left:412px;top:48px;display:flex;gap:26px;font-size:14px;color:#333}
.search{position:absolute;left:1062px;top:48px}

/* hero */
.hero{position:absolute;left:0;top:140px;width:1200px;height:580px;background:var(--hero)}
.hero .chair{left:150px;top:60px;width:420px;height:480px;background:radial-gradient(ellipse at 50% 45%,#a9a39c 0%,#cfc7bb 45%,#e4e4e4 75%)}
.hero-panel{position:absolute;left:597px;top:155px;width:603px;height:235px;background:var(--orange);color:var(--white);padding:28px 0 0 46px}
.hero-panel .kicker{font-size:13px}
.hero-panel h1{font-size:44px;font-weight:700;margin-top:2px}
.hero-panel p{font-size:13px;width:340px;margin-top:6px;line-height:1.4}
.hero-panel .shop{position:relative;display:inline-block;margin-top:14px;background:var(--blue);font-size:12px;padding:6px 16px}

/* feature product */
.tabs{position:absolute;left:0;top:828px;width:1200px;display:flex;justify-content:center;gap:24px;font-size:13px;color:#555}
.tabs .active{color:var(--blue);border-bottom:2px solid var(--blue)}
.side-label{position:absolute;font-size:14px;color:#777;transform:rotate(-90deg);transform-origin:center}
.product-caption{position:absolute;left:0;width:1200px;text-align:center;font-size:13px;color:#555}

/* services */
.services{position:absolute;left:0;top:1388px;width:1200px;height:405px;display:flex}
.service{position:relative;width:400px;height:405px;color:var(--white);text-align:center}
.service h3{position:absolute;top:170px;left:0;width:100%;font-size:30px;font-weight:700}
.service small{position:absolute;top:212px;left:0;width:100%;font-size:13px}
.service .view{position:absolute;top:335px;left:0;width:100%;font-size:13px}
.svc-res{background:linear-gradient(135deg,#6f604e,#9c8b74 50%,#4d4234)}
.svc-com{background:var(--orange)}
.svc-fur{background:linear-gradient(135deg,#3a3530,#a48d73 55%,#d9c5a8)}

/* latest */
.latest-card{position:absolute;top:1924px;width:190px;height:188px}
.latest-name{position:absolute;top:2128px;width:190px;text-align:center;font-size:12px;color:#555;line-height:1.6}

/* about */
.about{position:absolute;left:0;top:2296px;width:1200px;height:386px;background:var(--blue);color:var(--white)}
.about h2{position:absolute;left:124px;top:78px;font-size:30px;font-weight:700}
.about p{position:absolute;left:124px;width:420px;font-size:13px;line-height:1.45}
.about .more{position:absolute;left:124px;top:290px;background:var(--white);color:var(--ink);font-size:12px;padding:6px 10px}
.about .portrait{left:704px;top:27px;width:302px;height:359px;background:linear-gradient(160deg,#f2f2f2,#bdbdbd 60%,#6d6d6d)}

/* virtual reality */
.vr{position:absolute;left:0;top:2682px;width:1200px;height:754px;background:#eeeeee}
.vr .stage{left:235px;top:134px;width:730px;height:368px;background:linear-gradient(180deg,#d8d2c6 0%,#c8beae 62%,#a2744a 63%,#8a5d38 100%)}
.vr .stage-label{position:absolute;left:262px;top:150px;font-size:18px;font-weight:700;color:#333}
.thumb{position:absolute;top:519px;width:172px;height:168px;background:var(--white)}
.thumb i{position:absolute;left:14px;top:48px;width:144px;height:70px;display:block}
.arrow{position:absolute;top:590px;font-size:26px;color:var(--orange);font-weight:700}

/* news */
.news-card{position:absolute;top:3560px;width:310px;height:389px}
.news-card .img{left:0;top:0;width:310px;height:194px}
.news-card .date{position:absolute;left:14px;top:90px;width:58px;height:58px;background:var(--blue);color:var(--white);font-size:11px;text-align:center;padding-top:10px;line-height:1.4}
.news-card .body{position:absolute;left:0;top:194px;width:310px;height:195px;background:var(--orange);color:var(--white);padding:24px 24px 0}
.news-card h4{font-size:18px;font-weight:700}
.news-card p{font-size:13px;line-height:1.45;margin-top:10px}
.news-card .read{position:absolute;right:24px;bottom:30px;font-size:12px}

/* contact */
.contact{position:absolute;left:0;top:4096px;width:1200px;height:429px;background:var(--light)}
.field{position:absolute;background:var(--blue);color:var(--white);font-size:12px;padding:14px 14px}
.submit{position:absolute;left:526px;top:315px;width:154px;height:47px;background:var(--orange);color:var(--white);font-size:12px;font-weight:500;display:flex;align-items:center;justify-content:center}

/* perks */
.perks{position:absolute;left:0;top:4552px;width:1200px;height:91px;display:flex;justify-content:center;gap:0}
.perk{position:relative;width:240px;display:flex;align-items:center;gap:10px;padding-left:34px}
.perk b{display:block;font-size:14px;font-weight:700;color:var(--blue)}
.perk span{font-size:11px;color:#666}

/* footer */
.footer{position:absolute;left:0;top:4683px;width:1200px;height:278px;background:var(--footer);color:#ccc}
.footer .f-brand{position:absolute;left:124px;top:44px}
.footer .f-brand .mark{width:60px;height:60px;background:var(--orange)}
.footer .f-brand p{font-size:12px;line-height:1.45;width:190px;margin-top:14px}
.footer .f-brand .rm{font-size:12px;margin-top:10px;display:block}
.footer h5{position:absolute;top:40px;font-size:17px;font-weight:700;color:var(--white)}
.footer ul{position:absolute;top:84px;list-style:none;font-size:12px;line-height:2.1}
.subscribe{position:absolute;left:810px;top:148px;width:188px;height:34px;background:var(--white);display:flex}
.subscribe span{flex:1;font-size:11px;color:#888;padding:10px}
.subscribe i{width:42px;background:var(--orange)}
.bottombar{position:absolute;left:0;top:4961px;width:1200px;height:67px;background:var(--footer-deep);color:#ccc;font-size:12px}
.bottombar p{position:absolute;left:124px;top:26px}
.live-chat{position:absolute;left:838px;top:4961px;width:234px;height:67px;background:var(--orange);color:var(--white);font-size:18px;font-weight:700;display:flex;align-items:center;padding-left:22px;gap:12px}
</style>
</head>
<body>

<header class="topbar">
  <span class="phone">+00 555 210 48</span>
  <div class="social"><span></span><span></span><span></span><span></span></div>
  <div class="auth"><span class="signin">Sign in</span><span class="login">Login</span></div>
</header>

<nav class="nav">
  <div class="brand"><div class="mark"></div><div class="name">LORIVEL HOME STUDIO</div></div>
  <div class="menu"><span>Home</span><span>About</span><span>Services</span><span>Shop</span><span>Blog</span><span>Contact</span></div>
  <svg class="search" width="16" height="16" viewBox="0 0 16 16"><circle cx="6.5" cy="6.5" r="5" fill="none" stroke="#555" stroke-width="1.6"/><line x1="10.2" y1="10.2" x2="15" y2="15" stroke="#555" stroke-width="1.6"/></svg>
</nav>

<section class="hero">
  <div class="photo chair" role="img" aria-label="Upholstered armchair with grey seat and light wooden legs"></div>
  <div class="hero-panel">
    <div class="kicker">Collection 2018</div>
    <h1>Comfotable Chair</h1>
    <p>Lorem Ipsum is simply dummy text of the printing and typesetting industry.</p>
    <span class="shop">Shop Now</span>
  </div>
</section>

<h2 class="section-title" style="top:778px">Feature Product</h2>
<div class="tabs"><span class="active">Furniture</span><span>Lighting</span><span>Decor</span><span>Gifts</span><span>Textiles</span></div>
<span class="side-label" style="left:36px;top:968px">Prev</span>
<span class="side-label" style="left:1122px;top:968px">Next</span>
<div class="photo" style="left:185px;top:905px;width:110px;height:190px;background:linear-gradient(180deg,#f4f4f4,#dcdcdc)" role="img" aria-label="White side chair, faded"></div>
<div class="photo" style="left:405px;top:888px;width:390px;height:218px;background:linear-gradient(180deg,#c9c2b8 0%,#a9a194 40%,#b5954f 100%)" role="img" aria-label="Pair of upholstered stools with brass legs"></div>
<div class="photo" style="left:870px;top:905px;width:140px;height:170px;background:linear-gradient(180deg,#ece4dc,#d7b9b0)" role="img" aria-label="Ornate chair with red seat, faded"></div>
<div class="product-caption" style="top:1143px">Product Name<br>$ 540.00</div>
<div class="btn" style="left:558px;top:1213px;width:84px;height:30px">View More</div>

<h2 class="section-title" style="top:1314px">Our Services</h2>
<div class="services">
  <div class="service svc-res" role="img" aria-label="Residential bedroom interior"><h3>Residential</h3><small>Interior Design</small></div>
  <div class="service svc-com" role="img" aria-label="Commercial office interior with orange overlay"><h3>Commercial</h3><small>Interior Design</small><span class="view">View Collection</span></div>
  <div class="service svc-fur" role="img" aria-label="Craftsman finishing a wooden furniture piece"><h3>Furniture</h3><small>Design</small></div>
</div>

<h2 class="section-title" style="top:1844px">Latest Products</h2>
<span class="side-label" style="left:36px;top:2006px">Prev</span>
<span class="side-label" style="left:1122px;top:2006px">Next</span>
<div class="photo latest-card" style="left:208px;background:linear-gradient(180deg,#f2f2f2,#dedede)"><div class="photo" style="left:25px;top:60px;width:140px;height:70px;background:linear-gradient(90deg,#1c4f9e,#3c7fd6)" role="img" aria-label="Blue chaise lounge"></div></div>
<div class="photo latest-card" style="left:402px;background:linear-gradient(180deg,#f2f2f2,#dedede)"><div class="photo" style="left:45px;top:45px;width:100px;height:100px;background:linear-gradient(135deg,#c9c3a8,#8e8a6c)" role="img" aria-label="Textured cushion"></div></div>
<div class="photo latest-card" style="left:596px;background:linear-gradient(180deg,#f2f2f2,#dedede)"><div class="photo" style="left:55px;top:30px;width:80px;height:130px;background:linear-gradient(180deg,#7a5a3a,#3e2a1a)" role="img" aria-label="Round wooden side table"></div></div>
<div class="photo latest-card" style="left:804px;background:linear-gradient(180deg,#f2f2f2,#dedede)"><div class="photo" style="left:45px;top:25px;width:100px;height:140px;background:linear-gradient(180deg,#c4a27a,#7c5a3c)" role="img" aria-label="Carved decorative lantern"></div></div>
<div class="latest-name" style="left:208px">Product Name<br>$ 100.00</div>
<div class="latest-name" style="left:402px">Product Name<br>$ 90.00</div>
<div class="latest-name" style="left:596px">Product Name<br>$ 150.00</div>
<div class="latest-name" style="left:804px">Product Name<br>$ 170.00</div>
<div class="btn" style="left:558px;top:2212px;width:84px;height:28px">View More</div>

<section class="about">
  <h2>About Us</h2>
  <p style="top:128px">Lorivel Home Studio is a full service interior design firm led by principal designer Lori Velhane.</p>
  <p style="top:175px">As a child, Lori would spend quality time with her father by helping out in his furniture workshop. She was delighted to be seen sizing up project installations to exciting pieces like the cottage and other high-end hotels. What began as a fun after school activity evolved into a passion for furniture &amp; interior design and quality materials.</p>
  <span class="more">Read More</span>
  <div class="photo portrait" role="img" aria-label="Portrait of the principal designer"></div>
</section>

<section class="vr">
  <h2 class="section-title" style="top:64px">Virtual Reality</h2>
  <div class="photo stage" role="img" aria-label="Room render with grey tufted sofa, floor lamp and wooden floor"></div>
  <span class="stage-label">Product Name</span>
  <svg class="abs" style="left:902px;top:456px" width="28" height="28" viewBox="0 0 28 28"><path d="M3 10V3h7M18 3h7v7M25 18v7h-7M10 25H3v-7" fill="none" stroke="#fff" stroke-width="2"/></svg>
  <span class="arrow" style="left:205px">&#8592;</span>
  <span class="arrow" style="left:978px">&#8594;</span>
  <div class="thumb" style="left:235px"><i role="img" aria-label="Dark sideboard" style="background:linear-gradient(90deg,#3a3a3a,#6a6a6a)"></i></div>
  <div class="thumb" style="left:419px"><i role="img" aria-label="Grey chaise" style="background:linear-gradient(90deg,#8e8e8e,#c4c4c4)"></i></div>
  <div class="thumb" style="left:603px"><i role="img" aria-label="Navy sofa" style="background:linear-gradient(90deg,#1b2d5a,#34518f)"></i></div>
  <div class="thumb" style="left:788px"><i role="img" aria-label="Patterned sofa" style="background:linear-gradient(90deg,#4b5a6b,#9aa6b2)"></i></div>
</section>

<h2 class="section-title" style="top:3480px">News &amp; Events</h2>
<article class="news-card" style="left:121px">
  <div class="photo img" role="img" aria-label="Decorated dining interior" style="background:linear-gradient(135deg,#3f3a26,#8e7a4e)"></div>
  <div class="date">March 4<br>2018</div>
  <div class="body"><h4>News 1</h4><p>Lorem Ipsum is simply dummy text of the printing and typesetting industry.</p><span class="read">Read More...</span></div>
</article>
<article class="news-card" style="left:446px">
  <div class="photo img" role="img" aria-label="Living room with fireplace" style="background:linear-gradient(135deg,#5a3a2a,#b48a68)"></div>
  <div class="date">March 4<br>2018</div>
  <div class="body"><h4>News 2</h4><p>Lorem Ipsum is simply dummy text of the printing and typesetting industry.</p><span class="read">Read More...</span></div>
</article>
<article class="news-card" style="left:771px">
  <div class="photo img" role="img" aria-label="Outdoor terrace overlooking the sea" style="background:linear-gradient(180deg,#8ab0d0,#d9d2c2 60%,#8a7658)"></div>
  <div class="date">March 4<br>2018</div>
  <div class="body"><h4>News 2</h4><p>Lorem Ipsum is simply dummy text of the printing and typesetting industry.</p><span class="read">Read More...</span></div>
</article>
<div class="btn" style="left:558px;top:4009px;width:84px;height:28px">View More</div>

<section class="contact">
  <h2 class="section-title" style="top:34px">Contact Us</h2>
  <div class="field" style="left:124px;top:107px;width:305px;height:47px">Full Name</div>
  <div class="field" style="left:446px;top:107px;width:308px;height:47px">E-Mail</div>
  <div class="field" style="left:774px;top:107px;width:309px;height:47px">Phone</div>
  <div class="field" style="left:124px;top:171px;width:959px;height:124px">Message</div>
  <div class="submit">SUBMIT</div>
</section>

<div class="perks">
  <div class="perk"><svg width="26" height="20" viewBox="0 0 26 20"><rect x="1" y="3" width="15" height="11" fill="none" stroke="#0255a3" stroke-width="2"/><path d="M16 7h5l4 4v3h-9z" fill="none" stroke="#0255a3" stroke-width="2"/><circle cx="6" cy="16" r="2.5" fill="#0255a3"/><circle cx="20" cy="16" r="2.5" fill="#0255a3"/></svg><div><b>Free Shipping</b><span>Lorem Ipsum is simply text</span></div></div>
  <div class="perk"><svg width="22" height="22" viewBox="0 0 22 22"><path d="M4 9a7 7 0 0 1 13-3M18 13a7 7 0 0 1-13 3" fill="none" stroke="#0255a3" stroke-width="2"/><path d="M17 2v4h-4M5 20v-4h4" fill="none" stroke="#0255a3" stroke-width="2"/></svg><div><b>Free Exchange</b><span>30 Days Return Policy</span></div></div>
  <div class="perk"><svg width="22" height="22" viewBox="0 0 22 22"><circle cx="11" cy="11" r="9" fill="none" stroke="#0255a3" stroke-width="2"/><circle cx="11" cy="11" r="3.5" fill="none" stroke="#0255a3" stroke-width="2"/></svg><div><b>Premium Support</b><span>24/7 Customer service</span></div></div>
  <div class="perk"><svg width="24" height="18" viewBox="0 0 24 18"><rect x="1" y="1" width="22" height="16" rx="2" fill="none" stroke="#0255a3" stroke-width="2"/><line x1="1" y1="6" x2="23" y2="6" stroke="#0255a3" stroke-width="3"/></svg><div><b>Payment Method</b><span>Cash On Delivery</span></div></div>
</div>

<footer class="footer">
  <div class="f-brand"><div class="mark"></div><p>Lorivel Home Studio is a full service interior design firm led by principal designer Lori Velhane.</p><span class="rm">Read More...</span></div>
  <h5 style="left:404px">QUICK LINK</h5>
  <ul style="left:404px"><li>Home</li><li>About</li><li>Shop</li><li>Blog</li></ul>
  <h5 style="left:606px">SERIVECS</h5>
  <ul style="left:606px"><li>Residential Interior</li><li>Commercial Interior</li><li>Furniture Design</li></ul>
  <h5 style="left:810px">SUBSCRIBE</h5>
  <div class="subscribe"><span>Your E-Mail</span><i></i></div>
</footer>
<div class="bottombar"><p>CopyRight © 2018 LORIVEL HOME STUDIO. All Right Reserve</p></div>
<div class="live-chat"><svg width="24" height="20" viewBox="0 0 24 20"><path d="M2 2h20v12H9l-5 4v-4H2z" fill="#0255a3"/></svg>LIVE CHAT<svg width="12" height="8" viewBox="0 0 12 8" style="margin-left:24px"><path d="M1 1l5 6 5-6z" fill="#fff"/></svg></div>

</body>
</html>
```